Lumora business card for a plastic surgeon

we need a business card for plastic surgeons that work on a clinic called LUMORA.
we want a clean design and the following informations: name of the doctor, doctor's registration number (called CRM), telephone, address, facebook, instagram.
Colors: white, blue tones, light brown/ coffee

facebook and instagram: lumoracirurgiaestetica

Industry/Entity Type

Business

Contact Information for Business Card

clean design

Font styles to use
Serif
Sans Serif
Other font styles liked:
• helvetica light

Colors
cee9f5
85cae6
85abd2
3276b5
cfeae6
cedeed
eaf1f7

Requirements
Must have
• doctor's name
• identification number (called CRM)
• contact (phone, facebook, instagram, address)

```html
<!DOCTYPE html>
<html lang="pt">
<head>
<meta charset="utf-8">
<title>Lumora – Business Card</title>
<link rel="stylesheet" href="https://fonts.googleapis.com/css2?family=Marcellus&family=Marcellus+SC&family=Open+Sans:wght@300;400&display=swap">
<style>
  :root {
    --backdrop: #262524;
    --navy: #14365f;
    --cyan: #2ab7e2;
    --coffee: #b8977e;
    --silver-light: #e6e7e9;
    --silver-mid: #b4b6ba;
    --silver-dark: #8c8e93;
  }
  * { box-sizing: border-box; margin: 0; padding: 0; }
  html, body {
    width: 1200px; height: 1200px; overflow: hidden;
    background: var(--backdrop);
  }
  .sheet {
    position: relative; width: 1200px; height: 1200px;
  }
  .card {
    position: absolute; left: 160px; width: 880px; height: 500px;
    background: var(--navy); overflow: hidden;
    box-shadow: 0 8px 24px rgba(0,0,0,.45);
  }
  .card--back { top: 70px; }
  .card--front { top: 630px; }

  .foil {
    position: absolute; top: 0; height: 100%;
    background: linear-gradient(135deg, var(--silver-dark) 0%, var(--silver-light) 45%, var(--silver-mid) 75%, var(--silver-dark) 100%);
  }
  .card--back .foil { left: 0; width: 270px; }
  .card--front .foil { right: 0; width: 240px; }

  /* Back side */
  .social {
    position: absolute; left: 420px; top: 190px;
    list-style: none;
    font-family: "Open Sans", sans-serif; font-weight: 400;
    font-size: 22px; color: var(--coffee);
  }
  .social li { display: flex; align-items: center; gap: 12px; margin-bottom: 10px; }
  .chip {
    width: 24px; height: 24px; border-radius: 4px; background: var(--cyan); flex: none;
  }

  /* Front side */
  .brand {
    position: absolute; left: 50px; top: 40px;
  }
  .brand__name {
    font-family: "Marcellus", serif; font-size: 96px; line-height: 1;
    color: var(--cyan); letter-spacing: 2px;
  }
  .brand__tagline {
    font-family: "Marcellus", serif; font-size: 36px; line-height: 1.1;
    color: var(--coffee); letter-spacing: 1px; margin-left: 4px;
  }
  .doctor {
    position: absolute; left: 50px; top: 215px;
  }
  .doctor__name {
    font-family: "Marcellus SC", serif; font-size: 34px; color: var(--cyan); letter-spacing: 1px;
  }
  .doctor__crm {
    font-family: "Open Sans", sans-serif; font-weight: 300; font-size: 18px; color: var(--coffee);
    margin-top: 2px;
  }
  .divider {
    position: absolute; left: 50px; top: 322px; width: 330px; height: 1px; background: var(--cyan);
  }
  .contact {
    position: absolute; left: 50px; top: 345px; list-style: none;
    font-family: "Open Sans", sans-serif; font-weight: 300; font-size: 19px; color: var(--coffee);
  }
  .contact li { display: flex; align-items: center; gap: 14px; margin-bottom: 8px; }
  .contact svg { flex: none; }
  .address {
    position: absolute; left: 50px; top: 440px;
    font-family: "Open Sans", sans-serif; font-weight: 400; font-size: 18px;
    color: var(--cyan); text-transform: uppercase; letter-spacing: .5px;
  }
</style>
</head>
<body>
<main class="sheet">

  <section class="card card--back" aria-label="Card back">
    <div class="foil" role="img" aria-label="Silver foil petal decoration"></div>
    <ul class="social">
      <li><span class="chip"></span>www.lumoracirurgiaestetica.com</li>
      <li><span class="chip"></span>/lumoracirurgiaestetica</li>
      <li><span class="chip"></span>#lumoracirurgiaestetica</li>
    </ul>
  </section>

  <section class="card card--front" aria-label="Card front">
    <div class="brand">
      <div class="brand__name">LUMORA</div>
      <div class="brand__tagline">CIRURGIA PLÁSTICA</div>
    </div>
    <div class="doctor">
      <div class="doctor__name">Dr. Marco Salles</div>
      <div class="doctor__crm">CRM 482 915</div>
    </div>
    <div class="divider"></div>
    <ul class="contact">
      <li>
        <svg width="22" height="22" viewBox="0 0 22 22" aria-hidden="true">
          <rect width="22" height="22" rx="4" fill="var(--cyan)"/>
          <path d="M7 5c-1 0-2 1-2 2 0 6 4 10 10 10 1 0 2-1 2-2l-3-2-2 1c-2-1-3-2-4-4l1-2-2-3z" fill="var(--navy)"/>
        </svg>
        210-555-0147
      </li>
      <li><span class="chip" style="width:22px;height:22px"></span>@lumoracirurgiaestetica</li>
    </ul>
    <div class="address">1840 Alder Rd., Suite C. San Antonio, TX. 78201</div>
    <div class="foil" role="img" aria-label="Silver foil petal decoration"></div>
  </section>

</main>
</body>
</html>
```